Energy cost saving website (job description rewritten!)

Job Type: WordPress design
Task Outline: Create a WordPress design
Task Description:
We are new business (Germany) in the market of saving costs by power-saving (name: 'wir-falten-eure-Wolkenbögen.de'). This is reached by changing the supplier, the use of LED bulbs, energy saving washing machines, stoves, microwaves, hairdryers, vacuum cleaners and the like - where all of these be selled or affiliated through the website maybe you will create for us.
Design parameters:
We want a serious design that embodies a feeling of honesty, competence and capability.
Visitors should particularly see that this site saves them money!
The home page mainly should act as a selector of possibilities saving money by power-saving, usage of LED bulbs and large energy saving household devices (washing machines, etc.)
Updates
Hello designers,
browsing through the PixelHarbors files of portfolios I found one header graphics which excites me. Please find it here: http://www.pixelharbor-example.net/design/482716/wordpress-design-by-tarek-olumide . Note: it is NOT the picture but the shadowing. So if you consider this in your concepts would be another 'nice-to-have'.
Thanks.
Target Market(s)
People looking out for saving money by power-saving.
Industry/Entity Type
Business
Requirements
Must have
- Look and feel of 'this site saves me money'!
Nice to have
- We love 3D effects, but its not a must have. We also like cartoons, but feel free to develop your own concept, please. An appropriate backgrond picture would be nice.
Should not have
- Some kind of these exaggerated smiling or handshaking photos. That bathetic symbols like money bills or coins stacks.

```html
<!DOCTYPE html>
<html lang="en">
<head>
<meta charset="utf-8">
<title>LumaVolt GmbH – Energy Saving</title>
<link href="https://fonts.googleapis.com/css2?family=Oswald:wght@400;500;600&family=Open+Sans:wght@400;700&family=Arimo:wght@400;700&display=swap" rel="stylesheet">
<style>
  :root{
    --ink:#111;
    --text:#555;
    --muted:#666;
    --gold:#d9a21b;
    --gold-light:#ffd862;
    --gold-deep:#f3b300;
    --orange:#e8891a;
    --orange-deep:#e46b1c;
    --red:#b0121b;
    --pale-yellow:#f7ee9f;
    --page-bg:#f0f0f0;
    --card-border:#c9c9c9;
    --footer:#000;
    --button-text:#5a3a00;
  }
  *{box-sizing:border-box;margin:0;padding:0}
  html,body{width:1166px;height:1200px;overflow:hidden;background:#fff}
  body{font-family:"Arimo",Arial,sans-serif;color:var(--text)}
  .page{position:absolute;left:0;top:0;width:950px;height:978px;transform:scale(1.22737);transform-origin:0 0;background:#fff}
  .abs{position:absolute}

  .brand{left:33px;top:30px;font-family:"Oswald",sans-serif;font-weight:600;font-size:36px;line-height:46px;color:var(--ink);letter-spacing:.3px}
  .search{left:617px;top:51px;width:297px;height:25px;border:1px solid #d5d5d5;background:#fff;font-size:11px;color:#888;padding:6px 9px}
  .search svg{position:absolute;right:6px;top:4px}

  .nav{left:0;top:98px;width:950px;height:44px;background:linear-gradient(#ffe08a 0%,var(--gold-deep) 45%,#f7be10 70%,#ffe28f 100%);border-top:1px solid #e3a600;border-bottom:1px solid #c58d00;display:flex}
  .nav a{display:flex;align-items:center;justify-content:center;color:#000;text-decoration:none;font-size:14.5px;border-right:1px solid #c8960a;height:100%}
  .nav a:last-child{border-right:0}

  .hero{left:0;top:142px;width:950px;height:269px;background:linear-gradient(#3c3c3c 0%,#2a2a2a 40%,#111 75%,#050505 100%);border:1px solid #000}
  .offer{left:23px;width:303px;height:74px;border-radius:12px;border:1px solid #111;background:linear-gradient(#6e6e6e,#4a4a4a 50%,#3e3e3e);box-shadow:inset 0 1px 0 #8a8a8a;font-family:"Oswald",sans-serif;font-size:23px;color:var(--pale-yellow);display:flex;align-items:center;justify-content:center;letter-spacing:.5px}
  .offer-one{top:187px}
  .offer-two{top:278px}
  .more-offers{left:232px;top:366px;font-family:"Oswald",sans-serif;font-size:14px;color:#fff;text-decoration:underline}

  .banner{left:361px;top:201px;width:562px;height:198px;background:linear-gradient(90deg,#eef2e2,#f8faf1 60%,#f2f5e8);border:1px solid #cfd6bd}
  .bulb-photo{left:372px;top:155px;width:133px;height:250px;border-radius:50px 50px 20px 20px;background:linear-gradient(90deg,#9aa0a0,#eef0ee 35%,#ffffff 55%,#c4c8c6)}
  .tagline-1{left:521px;top:254px;font-family:"Open Sans",sans-serif;font-size:34px;color:var(--gold);letter-spacing:-.5px}
  .tagline-1 strong{font-weight:700}
  .tagline-2{left:558px;top:313px;font-family:"Open Sans",sans-serif;font-weight:700;font-size:26px;color:var(--orange-deep);letter-spacing:-.3px}

  .content{left:0;top:411px;width:950px;height:465px;background:linear-gradient(#e9e9e9,#f6f6f6 40%,#f3f3f3)}
  .welcome{left:44px;top:468px;font-family:"Oswald",sans-serif;font-weight:500;font-size:30px;color:var(--muted);letter-spacing:.5px}
  .welcome span{color:var(--gold)}
  .intro{left:44px;top:533px;width:480px;font-size:12px;line-height:22px}

  .read-more{width:103px;height:24px;border-radius:12px;background:linear-gradient(#f3c43a,#d49a0d);border:1px solid #b98506;font-family:"Oswald",sans-serif;font-size:13px;color:var(--button-text);display:flex;align-items:center;justify-content:center;gap:7px}
  .read-more::after{content:"";border-left:7px solid var(--button-text);border-top:5px solid transparent;border-bottom:5px solid transparent}

  .featured-title{left:60px;top:664px;font-family:"Oswald",sans-serif;font-weight:500;font-size:23px;color:var(--red);letter-spacing:.4px}
  .card{border:1px solid var(--card-border);border-radius:12px;background:linear-gradient(#fff,#f1f1f1)}
  .featured-card{left:43px;top:699px;width:535px;height:137px}
  .featured-photo{left:61px;top:719px;width:133px;height:97px;background:radial-gradient(ellipse at 60% 50%,#f4f4f4 0%,#9a9a9a 40%,#111 80%)}
  .featured-text{left:205px;top:727px;width:355px;font-size:11px;line-height:16px}

  .products-card{left:598px;top:450px;width:302px;height:386px;border-radius:14px}
  .products-title{left:636px;top:474px;font-family:"Oswald",sans-serif;font-weight:500;font-size:29px;color:var(--orange);letter-spacing:.5px}
  .product-list{left:648px;top:532px;list-style:none}
  .product-list li{height:34px;font-size:12.5px;color:#333;display:flex;align-items:center;gap:13px;line-height:16px;padding-bottom:14px}
  .product-list li::before{content:"";width:9px;height:7px;background:var(--orange);clip-path:polygon(0 30%,55% 30%,55% 0,100% 50%,55% 100%,55% 70%,0 70%)}

  .footer{left:0;top:876px;width:950px;height:102px;background:var(--footer);color:#fff}
  .footer a{position:absolute;top:13px;font-size:11px;color:#fff;text-decoration:none}
  .copyright{position:absolute;left:20px;top:39px;font-size:11px;color:#ddd}
  .powered{position:absolute;left:770px;top:16px;font-size:11px;color:#fff}
  .powered u{color:#fff}
</style>
</head>
<body>
<div class="page">
  <header>
    <div class="abs brand">LumaVolt GmbH</div>
    <div class="abs search">Search
      <svg width="16" height="16" viewBox="0 0 16 16"><circle cx="9.5" cy="6.5" r="4.5" fill="none" stroke="#333" stroke-width="1.5"/><line x1="6.3" y1="9.7" x2="1.5" y2="14.5" stroke="#333" stroke-width="2"/></svg>
    </div>
    <nav class="abs nav">
      <a style="width:143px">HOME</a>
      <a style="width:152px">ABOUT US</a>
      <a style="width:159px">SERVICES</a>
      <a style="width:169px">PRODUCTS</a>
      <a style="width:142px">OFFERS</a>
      <a style="width:185px">CONTACT US</a>
    </nav>
  </header>

  <section class="abs hero"></section>
  <div class="abs offer offer-one">&lt;&lt;&nbsp; Offer One &nbsp;&gt;&gt;</div>
  <div class="abs offer offer-two">&lt;&lt;&nbsp; Offer Two &nbsp;&gt;&gt;</div>
  <a class="abs more-offers">more offers...</a>
  <div class="abs banner"></div>
  <div class="abs bulb-photo" role="img" aria-label="Photo of a large white LED corn bulb with screw base"></div>
  <div class="abs tagline-1">We are <strong>energy saving</strong></div>
  <div class="abs tagline-2">and cost cutting company</div>

  <main>
    <div class="abs content"></div>
    <h1 class="abs welcome">Welcome to <span>Our Company!</span></h1>
    <p class="abs intro">This we achieve by changing the suppliers use LED bulbs, microwaves, hairdryers, vaccum cleaners to use LED bulbs This we achieve by changing the suppliers use LED bulbs, microwaves, hairdryers, vaccum cleaners to use LED bulbs</p>
    <div class="abs read-more" style="left:440px;top:613px">read more</div>

    <h2 class="abs featured-title">Featured Services</h2>
    <div class="abs card featured-card"></div>
    <div class="abs featured-photo" role="img" aria-label="Photo of a glowing white LED bulb on black"></div>
    <p class="abs featured-text">This we achieve by changing the suppliers use LED bulbs, microwaves, hairdryers, vaccum cleaners to use LED bulbs This we achieve by changing the suppliers use LED bulbs, microwaves, hairdryers, vaccum cleaners to use LED bulbs</p>
    <div class="abs read-more" style="left:440px;top:818px">read more</div>

    <aside>
      <div class="abs card products-card"></div>
      <h2 class="abs products-title">Our Products</h2>
      <ul class="abs product-list">
        <li>LED BULBS</li>
        <li>MICROWAVES</li>
        <li>HAIRDRYERS</li>
        <li>VACCUM CLEANERS</li>
        <li>MICROWAVES</li>
        <li>HAIRDRYERS</li>
        <li>VACCUM CLEANERS</li>
        <li>LED BULBS</li>
      </ul>
      <div class="abs read-more" style="left:766px;top:818px">read more</div>
    </aside>
  </main>

  <footer class="abs footer">
    <a style="left:21px">Home</a>
    <a style="left:89px">About Us</a>
    <a style="left:178px">Services</a>
    <a style="left:260px">Products</a>
    <a style="left:353px">Offers</a>
    <a style="left:425px">Contact Us</a>
    <div class="copyright">© Copyright 2012 LumaVolt. All rights reserved.</div>
    <div class="powered">Powered by: <u>Brightfold Studio</u></div>
  </footer>
</div>
</body>
</html>
```